Business Card Design

The image I attached was a quick thought to my design. I have triplets and was invisioning something with three figures with maybe the colors blue, pink and green. I would like it to look very chic and modern yet soothing/healing. I will take any fresh ideas as well.

Side 1: Contact Details
Side 2: Appointment section (mandatory)
Updates

Thank u all for your preliminary designs. I had sent the old design over and am looking for a bold fresh NEW LOOK  for CORE MOTION. I saw some really creative ideas in the gallery. If you have any other questions please feel free to email me at rtbwakes@quellmail.net.

Thanks

Please keep in mind that it is mandatory that on the back of the card is for appointments.

Thank you.

Reason: The two mandatory elements that need to be on the card is that her title needs to read as so:

Reason: The criteria is still not being met. Her title needs to read as so: Dr. Marisa Kettner, P.T., D.P.T. Doctor of Physical Therapy and The appointment info must go on the BACK of the card. Looking forward to some more great designs. Thanks.

Industry/Entity Type

Business

Contact Information for Business Card

Core Motion
Physical & Aquatic Therapy
Dr. Marisa Kettner, P.T., D.P.T.
Doctor of Physical Therapy

22-48 B Birchwick Lane
Elmbury, N.Y. 11592
(Located inside of the Summit gym in the Pinecrest shopping center)

Phone & Fax: (631) 555-0172
Mkettner4@harbornet.net

Requirements
Must have
• One the back I would like to do an appointment layout.

```html
<!DOCTYPE html>
<html lang="en">
<head>
<meta charset="utf-8">
<title>Core Motion – Business Card</title>
<link rel="stylesheet" href="https://fonts.googleapis.com/css2?family=Poppins:wght@300;400;600&display=swap">
<style>
  :root {
    --bg: #e9eaec;
    --card: #ffffff;
    --green: #a6cd39;
    --blue: #a9dde3;
    --pink: #d83a7c;
    --ink-dark: #4a4a4a;
    --ink-mid: #6b6b6b;
    --ink-light: #9a9a9a;
    --rule: #d9d9d9;
    --photo-a: #7e9c96;
    --photo-b: #c9c3bd;
  }
  * { margin: 0; padding: 0; box-sizing: border-box; }
  html, body { width: 1200px; height: 1000px; overflow: hidden; }
  body { background: var(--bg); font-family: "Poppins", sans-serif; position: relative; }

  .card {
    position: absolute; left: 250px; width: 700px; height: 400px;
    background: var(--card); border-radius: 22px; overflow: hidden;
    box-shadow: 0 10px 30px rgba(0,0,0,0.12);
  }
  .card--front { top: 70px; }
  .card--back { top: 530px; }
  .block { position: absolute; }

  /* front: contact details */
  .brand { position: absolute; left: 56px; top: 48px; }
  .brand__name { font-weight: 600; font-size: 25px; color: var(--ink-dark); letter-spacing: 0.5px; line-height: 1.15; }
  .brand__tag { font-weight: 400; font-size: 23px; color: var(--green); line-height: 1.25; }
  .person { position: absolute; left: 76px; top: 130px; }
  .person__name { font-weight: 600; font-size: 22px; color: var(--ink-dark); line-height: 1.25; }
  .person__title { font-weight: 400; font-size: 20px; color: var(--ink-mid); line-height: 1.25; }
  .address { position: absolute; left: 76px; top: 218px; font-size: 18px; color: var(--ink-mid); line-height: 1.4; }
  .reach { position: absolute; left: 420px; top: 220px; font-size: 16px; color: var(--ink-mid); line-height: 1.5; }
  .location { position: absolute; left: 76px; top: 290px; font-size: 16px; color: var(--ink-light); }
  .front-band { position: absolute; left: 0; top: 352px; width: 470px; height: 48px; background: var(--green); }

  /* back: brand + appointment */
  .photo {
    position: absolute; left: 0; top: 0; width: 700px; height: 190px;
    background: linear-gradient(120deg, var(--photo-a) 0%, #9fb3ad 55%, var(--photo-b) 100%);
  }
  .band { position: absolute; left: 0; top: 170px; width: 470px; height: 76px; background: var(--green); padding: 8px 0 0 60px; color: #fff; }
  .band__name { font-weight: 600; font-size: 27px; line-height: 1.15; letter-spacing: 0.5px; }
  .band__tag { font-weight: 400; font-size: 22px; line-height: 1.25; }
  .appt-title { position: absolute; left: 60px; top: 264px; font-weight: 600; font-size: 17px; color: var(--green); letter-spacing: 0.6px; }
  .appt-field { position: absolute; left: 60px; font-size: 18px; color: var(--ink-light); display: flex; align-items: flex-end; }
  .appt-field__label { width: 56px; }
  .appt-field__line { display: inline-block; width: 500px; border-bottom: 1px solid var(--rule); height: 1px; margin-bottom: 5px; }
  .appt-field--date { top: 304px; }
  .appt-field--time { top: 346px; }
</style>
</head>
<body>

<section class="card card--front" aria-label="Contact side">
  <div class="brand">
    <div class="brand__name">CORE MOTION</div>
    <div class="brand__tag">Physical &amp; Aquatic Therapy</div>
  </div>
  <div class="person">
    <div class="person__name">Dr. Marisa Kettner, P.T., D.P.T.</div>
    <div class="person__title">Doctor of Physical Therapy</div>
  </div>
  <div class="address">
    <div>22-48 B Birchwick Lane</div>
    <div>Elmbury, N.Y. 11592</div>
  </div>
  <div class="reach">
    <div>Phone &amp; Fax: (631) 555-0172</div>
    <div>Mkettner4@harbornet.net</div>
  </div>
  <div class="location">Located inside of the Summit gym in the Pinecrest shopping center</div>
  <div class="block" style="left:640px;top:316px;width:60px;height:40px;background:var(--pink)"></div>
  <div class="block" style="left:470px;top:334px;width:170px;height:66px;background:var(--blue)"></div>
  <div class="front-band"></div>
</section>

<section class="card card--back" aria-label="Appointment side">
  <div class="photo" role="img" aria-label="Photo of a therapist guiding an older patient through an aquatic therapy exercise in a pool"></div>
  <div class="block" style="left:640px;top:96px;width:60px;height:70px;background:var(--pink)"></div>
  <div class="block" style="left:470px;top:114px;width:170px;height:72px;background:var(--blue)"></div>
  <div class="band">
    <div class="band__name">CORE MOTION</div>
    <div class="band__tag">Physical &amp; Aquatic Therapy</div>
  </div>
  <div class="appt-title">APPOINTMENT DETAILS</div>
  <div class="appt-field appt-field--date"><span class="appt-field__label">Date:</span><span class="appt-field__line"></span></div>
  <div class="appt-field appt-field--time"><span class="appt-field__label">Time:</span><span class="appt-field__line"></span></div>
</section>

</body>
</html>
```